https://dorvakel.com

We need a cool technology design for our Managed IT Services company. We are located in Coral Springs Florida. We provide all IT services and support for small to medium sized businesses. We would like to see designs that use our blue and white colors from our website.

```html
<!DOCTYPE html>
<html lang="en">
<head>
<meta charset="utf-8">
<title>Dorvakel Business Card</title>
<link rel="stylesheet" href="https://fonts.googleapis.com/css2?family=Roboto:wght@400;700;900&family=Roboto+Condensed:wght@400;500&display=swap">
<style>
  :root {
    --canvas: #e9e6e1;
    --card: #f4f4f4;
    --navy: #0d2c54;
    --ink: #3a3a3a;
    --muted: #9a9a9a;
    --faint: #d5d8dc;
  }
  * { margin: 0; padding: 0; box-sizing: border-box; }
  html, body { width: 1200px; height: 960px; overflow: hidden; }
  body { background: var(--canvas); position: relative; font-family: "Roboto", sans-serif; }

  .card {
    position: absolute;
    width: 600px;
    height: 343px;
    background: var(--card);
    box-shadow: 0 2px 4px rgba(0,0,0,0.18);
  }
  .card--front { left: 314px; top: 113px; }
  .card--back  { left: 311px; top: 472px; }

  .brand-name {
    position: absolute;
    left: 54px;
    top: 50px;
    font-family: "Roboto", sans-serif;
    font-weight: 900;
    font-size: 45px;
    letter-spacing: -1.2px;
    color: var(--navy);
    line-height: 1;
  }

  .contact-block {
    position: absolute;
    right: 43px;
    top: 159px;
    text-align: right;
  }
  .person-name {
    font-family: "Roboto Condensed", sans-serif;
    font-weight: 500;
    font-size: 25px;
    color: var(--navy);
    line-height: 1;
  }
  .person-title {
    font-family: "Roboto Condensed", sans-serif;
    font-size: 15px;
    color: var(--muted);
    margin-top: 3px;
    letter-spacing: 0.3px;
  }
  .address {
    margin-top: 11px;
    font-size: 14.5px;
    line-height: 19px;
    color: var(--ink);
    font-style: normal;
  }
  .contact-list { list-style: none; margin-top: 10px; }
  .contact-list li {
    display: flex;
    justify-content: flex-end;
    align-items: center;
    gap: 9px;
    font-size: 14.5px;
    line-height: 19px;
    color: var(--ink);
  }
  .contact-list svg { width: 13px; height: 13px; fill: var(--navy); flex: none; }

  .back-mark {
    position: absolute;
    left: 0;
    right: 0;
    top: 132px;
    text-align: center;
    font-family: "Roboto", sans-serif;
    font-weight: 900;
    font-size: 60px;
    letter-spacing: -1px;
    line-height: 1;
    color: var(--faint);
  }

  .back-url {
    position: absolute;
    left: 0;
    right: 0;
    top: 284px;
    text-align: center;
    font-size: 15px;
    letter-spacing: 0.55em;
    color: #555;
  }
</style>
</head>
<body>
  <section class="card card--front">
    <div class="brand-name">DORVAKEL</div>
    <div class="contact-block">
      <div class="person-name">MARCUS HALE</div>
      <div class="person-title">CEO/FOUNDER</div>
      <address class="address">2280 Westbrook Ave #140<br>Coral Springs, Florida 33065</address>
      <ul class="contact-list">
        <li>(954) 555-0182
          <svg viewBox="0 0 16 16" aria-hidden="true"><path d="M3.6 1.2l2.3 2.6c.4.4.4 1 0 1.4L4.8 6.4c.8 1.8 2.9 3.9 4.8 4.8l1.2-1.1c.4-.4 1-.4 1.4 0l2.6 2.3c.4.4.4 1 0 1.4l-1.2 1.2C11.7 16.9 -.9 4.3 1 2.4l1.2-1.2c.4-.4 1-.4 1.4 0z"/></svg>
        </li>
        <li>marcus@dorvakel.com
          <svg viewBox="0 0 16 16" aria-hidden="true"><path d="M1 3h14v1.2L8 8.6 1 4.2z"/><path d="M1 5.8l7 4.4 7-4.4V13H1z"/></svg>
        </li>
        <li>www.dorvakel.com
          <svg viewBox="0 0 16 16" aria-hidden="true"><circle cx="8" cy="8" r="7"/><path d="M1.5 8h13M8 1c2 2 2 12 0 14M8 1c-2 2-2 12 0 14" stroke="#f4f4f4" stroke-width="1.1" fill="none"/></svg>
        </li>
      </ul>
    </div>
  </section>

  <section class="card card--back">
    <div class="back-mark">DORVAKEL</div>
    <div class="back-url">www.dorvakel.com</div>
  </section>
</body>
</html>
```